Redesign of existing business card

I would like the "signage" attachment converted into a business card. This needs to be double sided aswell, keeping the phone number and names on the front, and the email + website on the back.

Second attachment is the current business card design.

Larger font for contact details is required.

Must keep to original color themes (electric blue, silver/grey etc)

Back of the card to have blue background with white writing.

Industry/Entity Type

Business

Contact Information for Business Card

Refer to existing design from attachments

Requirements
Must have
• Refer to existing design from attachments
Nice to have

```html
<!DOCTYPE html>
<html lang="en">
<head>
<meta charset="utf-8">
<title>Voltline Electrical Services – Business Card</title>
<link rel="stylesheet" href="https://fonts.googleapis.com/css2?family=Roboto:wght@400;500;700&display=swap">
<style>
  :root {
    --electric-blue: #1e22f2;
    --silver: #b9bcc2;
    --silver-dark: #7d8088;
    --white: #ffffff;
    --backdrop: #e6e7ea;
  }
  * { margin: 0; padding: 0; box-sizing: border-box; }
  html, body {
    width: 1200px; height: 950px; overflow: hidden;
    background: var(--backdrop);
    font-family: "Roboto", Arial, sans-serif;
  }
  .sheet { position: relative; width: 1200px; height: 950px; }
  .card {
    position: absolute; left: 250px; width: 700px; height: 400px;
    overflow: hidden;
    box-shadow: 0 8px 24px rgba(0,0,0,0.18);
  }
  .card--back { top: 50px; background: var(--electric-blue); }
  .card--front { top: 500px; background: var(--white); }

  .card-shapes { position: absolute; inset: 0; width: 100%; height: 100%; }

  .wordmark { position: absolute; display: flex; align-items: center; gap: 16px; }
  .wordmark__dot { width: 54px; height: 54px; border-radius: 50%; flex: none; }
  .wordmark__name {
    font-weight: 700; font-size: 34px; line-height: 1.05;
    letter-spacing: 0.5px; text-transform: uppercase;
  }
  .card--back .wordmark { left: 150px; top: 110px; }
  .card--back .wordmark__dot { background: var(--white); }
  .card--back .wordmark__name { color: var(--white); }
  .card--front .wordmark { left: 150px; top: 88px; }
  .card--front .wordmark__dot { background: var(--silver-dark); }
  .card--front .wordmark__name { color: var(--electric-blue); }

  .back-contacts {
    position: absolute; left: 0; right: 0; top: 248px;
    list-style: none; color: var(--white);
  }
  .back-contacts li {
    display: flex; justify-content: center; align-items: center;
    gap: 12px; font-size: 19px; letter-spacing: 1px; margin-bottom: 12px;
  }
  .back-contacts svg { width: 18px; height: 18px; flex: none; }

  .front-phone {
    position: absolute; right: 36px; top: 236px;
    display: flex; align-items: center; gap: 10px;
    color: var(--white); font-size: 20px;
  }
  .front-phone svg { width: 18px; height: 18px; flex: none; }

  .person { position: absolute; left: 48px; bottom: 42px; color: var(--white); }
  .person__name { font-size: 24px; font-weight: 500; text-transform: uppercase; }
  .person__role { font-size: 18px; margin-top: 2px; }
</style>
</head>
<body>
<main class="sheet">

  <section class="card card--back" aria-label="Back of business card">
    <div class="wordmark">
      <span class="wordmark__dot"></span>
      <span class="wordmark__name">Voltline<br>Electrical Services</span>
    </div>
    <ul class="back-contacts">
      <li>
        <svg viewBox="0 0 16 16"><rect x="1" y="3" width="14" height="10" rx="1" fill="#fff"/><path d="M1.5 3.5L8 9l6.5-5.5" fill="none" stroke="var(--electric-blue)" stroke-width="1.3"/></svg>
        sam@voltlineelectric.com
      </li>
      <li>
        <svg viewBox="0 0 16 16"><circle cx="8" cy="8" r="7" fill="#fff"/><path d="M1 8h14M8 1c3 3 3 11 0 14M8 1c-3 3-3 11 0 14" fill="none" stroke="var(--electric-blue)" stroke-width="1.1"/></svg>
        www.voltlineelectric.com.au
      </li>
    </ul>
  </section>

  <section class="card card--front" aria-label="Front of business card">
    <svg class="card-shapes" viewBox="0 0 700 400" preserveAspectRatio="none" aria-hidden="true">
      <defs>
        <linearGradient id="silverStrip" x1="0" y1="0" x2="1" y2="0">
          <stop offset="0" stop-color="#7d8088"/>
          <stop offset="1" stop-color="#b9bcc2"/>
        </linearGradient>
      </defs>
      <polygon points="0,0 90,0 0,70" fill="url(#silverStrip)"/>
      <polygon points="0,288 700,162 700,400 0,400" fill="#1e22f2"/>
    </svg>

    <div class="wordmark">
      <span class="wordmark__dot"></span>
      <span class="wordmark__name">Voltline<br>Electrical Services</span>
    </div>

    <p class="front-phone">555 0134 2260
      <svg viewBox="0 0 16 16"><path fill="#fff" d="M3 1.5l3 .5 1 3.5-1.8 1.3a8 8 0 0 0 4 4L10.5 9l3.5 1 .5 3-1.5 1.5C7 14.5 1.5 9 1.5 3z"/></svg>
    </p>

    <div class="person">
      <p class="person__name">Sam Ferris</p>
      <p class="person__role">President</p>
    </div>
  </section>

</main>
</body>
</html>
```